VESTRA電子書籍 表紙発注書

【依頼概要】

<サブタイトル>

小さな会社や個人事業でもできる!

<書籍タイトル>

数字が苦手な 店主のための
【看板づくり手帖】

※ターゲットの目にすぐ入る様に(小さな会社)(個人事業)(ネットに弱い)を目立つ様にお願いします。
※電子書籍なので表示される際の画像が小さいため、タイトルもできるだけ視認しやすい文字でお願いします。

<オビ部分>

ホームページを作る前に
必ずお読みください。

読者限定プレゼント付
●思わずポチッと押したくなる!
【段階別】キャッチコピーの作り方
●真似するだけでOK!
【ランディングページのテンプレート】

※プレゼントは目立つ様にお願いします。

<著者>

WEB集客のしくみ作りの専門家
森田 サキ

※著者似顔絵をどちらか使ってください。

<読者ターゲット層>
・40代~50代の、小規模企業の経営者・個人事業経営者・個人起業家

<イメージ>
・色の指定などはありません。
もし自分が起業する時なら、どんな表紙に目が止まるか考えてみていただけると嬉しいです。

・ビジネス書ではありますが、ターゲットはネットやパソコンに苦手意識を持っている経営者の方なので、また女性の起業家さんにも見て欲しいので、ちゃんとした雰囲気はありつつも、あまり硬くなく、自分でもできそうかなー、と思わせる様な雰囲気が出るといいなと思っています。
よろしくお願いいたします。

※著者似顔絵2点添付します。どちらかをお使いください。
※写真・イラスト素材購入の際は別途お支払いします。 その場合は、小サイズ画像で大丈夫です。

※参考資料として、まだ未完成ですが原稿を添付します。
パスワードがありますのでこちらで開いてください。

▶︎PDFを開く時のパスワード: demo1

《追記1》必ずご覧ください。
↓ ↓ ↓
書籍のタイトルとオビの文言をを変更しました。
申し訳ありませんが、こちらを必ずご確認ください。

(すでに提案をくださった方は、そのままのデザインで検討させていただきますので、再提出はしなくて大丈夫です。採用になった場合のみ変更のご依頼をさせていただきますが、その際は報酬をプラスさせていただきます※9/15日朝7時30分までに提案くださった方)

《変更内容》
<書籍タイトル>
帳簿が苦手な 店主のための
「街角で商売」

※ターゲットの目にすぐ入る様に(小さな会社)(個人事業)(ウェブに弱い)を目立つ様にお願いします。

<オビ部分>
※この本を読むまでは
ホームページは作らないでください。

▶︎参考本文(未完成)は新しい方(ファイル名:【原稿】こちらをご覧ください)
をご覧ください」
▶︎▶︎PDFファイルパスワード demo2
《追記2》
追記1にて一部変更をさせていただきましたが、
追記1の《変更内容》以外は最初の依頼内容通りなので、再度ご確認ください。

あと、少し気になったのですが、著者の似顔絵はメインビジュアルに使わなくて大丈夫です。名前の横にひっそりとつかう程度でいいかと思います。
もちろん、何か意図を持って使いたいという場合はご提案大歓迎です^ ^

▶︎必要な構成要素を再度まとめますね。
(読者ターゲットや希望デザインについては最初の依頼内容をご確認ください)
ーーーーーーーーーーーーーーーーーーー
<文字>
小さな会社や個人事業でもできる!

帳簿が苦手な 店主のための
「街角で商売」

※この本を読むまでは
ホームページは作らないでください。

読者限定プレゼント付
●思わずポチッと押したくなる!
【段階別 キャッチコピーの作り方】
●真似するだけでOK!
【ランディングページのテンプレート】

WEB集客のしくみ作りの専門家
森田 サキ

<画像>
著者似顔絵(メインビジュアルには使わなくていいいです)

※その他、写真・イラストの使用はお任せ

ーーーーーーーーーーーーーーーーーーー

こちらの説明不足のため誤解を招いてしまい、たいへん申し訳ございませんでした。

誰のための何の本ななのか、スマホでVestraを見た時でもはっきりわかるスッキリしたデザインがよかったです。また、こちらの要望通りに、ウェブが苦手な人や女性も、ついポチッと押してしまいそうなデザインでした。

選考には、20人ほどの方から意見をいただいたのですが、やはりはっきり文字が読み取れるものが人気が高かったです。
なるほどなぁ、と思ったのは、少しデザインの知識がある人(私を含め)と、とくにこだわりのない普通の人たちとでは、見る視点が違うのか、少し意見が別れました。読者目線がやはり大事ですね。

たくさんのご提案をいただき、本当にありがとうございました。

中には、さすがプロっぽいと思わせる作品や、手間をかけて作ってくださったと思われる作品もあり、本当にありがたく、また選考もかなり迷いました。

提案してくださった皆様、本当にありがとうございました。

```html
<!DOCTYPE html>
<html lang="ja">
<head>
<meta charset="utf-8">
<title>帳簿が苦手な 店主のための「街角で商売」</title>
<link href="https://fonts.googleapis.com/css2?family=Noto+Sans+JP:wght@500;700;900&display=swap" rel="stylesheet">
<style>
  :root {
    --sky-top: #cfe9f8;
    --sky-bottom: #eef8fd;
    --navy: #1b2a5a;
    --title-blue: #1570c8;
    --accent-red: #e5322b;
    --band-yellow: #ffe735;
    --dot-yellow: #f6c800;
    --paper: #ffffff;
    --desk-light: #f4fafe;
    --desk-mid: #d6ecf9;
    --desk-deep: #a9d3ee;
    --portrait-light: #f3d9c6;
    --portrait-deep: #8a5a3c;
  }
  html, body { margin: 0; padding: 0; overflow: hidden; }
  body { width: 750px; height: 1200px; background: var(--paper); }
  .cover {
    position: relative; width: 750px; height: 1200px; overflow: hidden;
    font-family: "Noto Sans JP", sans-serif; color: var(--navy);
    background: linear-gradient(180deg, var(--sky-top) 0%, var(--sky-bottom) 64%);
  }
  .desk-scene {
    position: absolute; left: 0; top: 0; width: 750px; height: 345px;
    background:
      radial-gradient(ellipse 260px 150px at 36% 38%, var(--desk-light) 0%, rgba(244,250,254,0) 100%),
      radial-gradient(ellipse 180px 120px at 70% 30%, var(--desk-light) 0%, rgba(244,250,254,0) 100%),
      linear-gradient(160deg, var(--desk-mid) 0%, var(--desk-deep) 100%);
  }
  .subtitle {
    position: absolute; right: 28px; top: 345px; margin: 0; text-align: right;
    font-weight: 900; font-size: 56px; line-height: 76px; letter-spacing: 1px;
  }
  .lead {
    position: absolute; left: 0; right: 0; top: 520px; margin: 0; text-align: center;
    font-weight: 900; font-size: 48px; line-height: 60px;
  }
  .lead .weak { color: var(--accent-red); font-size: 52px; margin-right: 12px; }
  .book-title {
    position: absolute; left: 0; right: 0; top: 598px; margin: 0; text-align: center;
    font-weight: 900; font-size: 96px; line-height: 120px; color: var(--title-blue);
    -webkit-text-stroke: 14px var(--paper); paint-order: stroke fill; letter-spacing: 2px;
  }
  .lower {
    position: absolute; left: 0; top: 770px; width: 750px; height: 430px; background: var(--paper);
  }
  .warning {
    position: absolute; left: 28px; top: 786px; margin: 0;
    font-weight: 900; font-size: 40px; line-height: 50px; color: var(--accent-red);
  }
  .warning .indent { display: block; padding-left: 42px; }
  .author-role {
    position: absolute; left: 496px; top: 792px; margin: 0;
    font-weight: 700; font-size: 26px; line-height: 40px;
  }
  .author-name {
    position: absolute; right: 26px; top: 902px; margin: 0;
    font-weight: 700; font-size: 34px; line-height: 46px; white-space: nowrap;
  }
  .author-name small { font-size: 24px; margin-left: 6px; }
  .author-portrait {
    position: absolute; left: 522px; top: 962px; width: 100px; height: 100px; border-radius: 50%;
    background: linear-gradient(160deg, var(--portrait-light) 0%, var(--portrait-deep) 100%);
  }
  .gift-band {
    position: absolute; left: 24px; top: 950px; width: 390px; height: 52px;
    background: var(--band-yellow); font-weight: 900; font-size: 36px; line-height: 52px;
    text-align: center; margin: 0;
  }
  .gifts { position: absolute; left: 28px; top: 1016px; margin: 0; padding: 0; list-style: none; }
  .gifts li { margin-bottom: 6px; }
  .gifts .hook {
    position: relative; padding-left: 42px; font-weight: 900; font-size: 30px; line-height: 42px;
  }
  .gifts .hook::before {
    content: ""; position: absolute; left: 4px; top: 9px; width: 24px; height: 24px;
    border-radius: 50%; background: var(--dot-yellow);
  }
  .gifts .item { padding-left: 32px; font-weight: 700; font-size: 28px; line-height: 40px; }
</style>
</head>
<body>
<main class="cover">
  <div class="desk-scene" role="img" aria-label="ノートパソコン、手帳、スマートフォン、眼鏡、コーヒー、観葉植物が並ぶ明るいデスクの写真"></div>

  <p class="subtitle">小さな会社や<br>個人事業でもできる!</p>
  <p class="lead"><span class="weak">帳簿が苦手な</span>店主のための</p>
  <h1 class="book-title">「街角で商売」</h1>

  <section class="lower"></section>
  <p class="warning">※この本を読むまでは<span class="indent">ホームページは</span><span class="indent">作らないでください。</span></p>

  <p class="author-role">WEB集客の<br>しくみ作りの専門家</p>
  <p class="author-name">森田 サキ<small>著</small></p>
  <div class="author-portrait" role="img" aria-label="著者の似顔絵"></div>

  <p class="gift-band">読者限定プレゼント付</p>
  <ul class="gifts">
    <li><div class="hook">思わずポチッと押したくなる!</div><div class="item">【段階別　キャッチコピーの作り方】</div></li>
    <li><div class="hook">真似するだけでOK!</div><div class="item">【ランディングページのテンプレート】</div></li>
  </ul>
</main>
</body>
</html>
```